Childrens Business Card Design Project

We have an existing logo attached which we'd like to use as part of our new business card design.

The design needs to be relatively gender neutral and contain bright colours.

In terms of look and feel think:

Fun, Modern, Quality (as opposed to cheap!) and of course Party!

Single or double sided - i am not decided on either one yet - ideally i'd like to see designs for both because if you think stylistically it would benefit having two sides then please try it out!

I think the challenge here is finding a really good background colour (if you think it needs one) and also choosing an eye grabbing text that compliments the existing logo - do that an you are onto a winner! I have another image for the business (which i have attached) which uses stripes so i am keen to see a design that incorporates this to tie in all my collateral.

The copy required is as follows (not necesarily in this order)

Bookings/Enquiries:

Tilda

T: 0498 765 210
E: enquiries@brixtopia.com.au

ABN: 43 527 806 214

Any feedback on text is welcomed - please message me or add to the discussion.

Reason: Hi All, I have received some promising designs, but overall i am not impressed with the quality of the work so have extended the deadline as this project has been committed. I will aim to attach some business card examples to the brief tomorrow to give further guidance as a whole but please do not submit any designs on a generic background that are not related to the theme, have been carelessly placed with overlapping elements - it just looks sloppy. For those who have read the brief an incorporated stripes or even spots this is on target as it convey's a party theme, however please work on getting the colours for the contact details by either a bold solid strip to highlight or some other way to frame it. When it comes to the logo, some people have removed the characters all together and changed the colour of the wording - this is fine. Also feel free to balloons starts - but keep it classy and watch your placement of these. I hope this helps and for the designs i would like to see revisions for i will aim to get back to you individually over the next day or so. Many thanks all.

Target Market(s)

Mothers in the suburbs of Australia with a disposal able income, children aged between 1-7 years old.

Industry/Entity Type

Business

Requirements
Must have
• The font and wording positioning must compliment the logo.

```html
<!DOCTYPE html>
<html lang="en">
<head>
<meta charset="utf-8">
<title>Brixtopia Business Card</title>
<link rel="stylesheet" href="https://fonts.googleapis.com/css2?family=Caprasimo&family=Andika:wght@400&display=swap">
<style>
  :root {
    --backdrop: #d9d9d9;
    --card: #ffffff;
    --pattern-teal: #7fcfd0;
    --pattern-pink: #f3a9cc;
    --pattern-yellow: #f6dc5c;
    --pattern-purple: #a8559f;
    --pattern-lime: #b9d55a;
    --brand-blue: #1f8fd8;
    --rule-blue: #2f8fd4;
    --name-orange: #f39a1e;
    --contact-red: #e3202c;
    --tagline-orange: #f2a24a;
    --band-tint: rgba(255, 255, 255, 0.85);
  }
  * { margin: 0; padding: 0; box-sizing: border-box; }
  html, body {
    width: 1200px;
    height: 900px;
    overflow: hidden;
    background: var(--backdrop);
  }
  .card {
    position: absolute;
    left: 160px;
    top: 170px;
    width: 880px;
    height: 560px;
    border-radius: 36px;
    background: var(--card);
    overflow: hidden;
    box-shadow: 0 18px 40px rgba(0, 0, 0, 0.18);
  }
  .card-pattern {
    position: absolute;
    inset: 0;
    background:
      radial-gradient(circle at 8% 62%, rgba(168, 85, 159, 0.55) 0, rgba(168, 85, 159, 0) 120px),
      radial-gradient(circle at 4% 30%, rgba(243, 169, 204, 0.6) 0, rgba(243, 169, 204, 0) 140px),
      radial-gradient(circle at 30% 2%, rgba(246, 220, 92, 0.45) 0, rgba(246, 220, 92, 0) 130px),
      radial-gradient(circle at 55% 4%, rgba(127, 207, 208, 0.55) 0, rgba(127, 207, 208, 0) 150px),
      radial-gradient(circle at 96% 14%, rgba(185, 213, 90, 0.55) 0, rgba(185, 213, 90, 0) 140px),
      radial-gradient(circle at 94% 55%, rgba(243, 169, 204, 0.5) 0, rgba(243, 169, 204, 0) 130px),
      radial-gradient(circle at 20% 100%, rgba(127, 207, 208, 0.7) 0, rgba(127, 207, 208, 0) 170px),
      radial-gradient(circle at 78% 100%, rgba(168, 85, 159, 0.5) 0, rgba(168, 85, 159, 0) 150px),
      radial-gradient(circle at 60% 98%, rgba(246, 220, 92, 0.6) 0, rgba(246, 220, 92, 0) 140px),
      var(--card);
  }
  .party-characters {
    position: absolute;
    left: 150px;
    top: 34px;
    width: 600px;
    height: 232px;
    border-radius: 24px;
    background: linear-gradient(90deg, #f59a9a 0%, #f7cf5a 50%, #7fb0d8 100%);
    opacity: 0.6;
  }
  .brand {
    position: absolute;
    left: 0;
    right: 0;
    top: 278px;
    text-align: center;
  }
  .brand-name {
    font-family: "Caprasimo", serif;
    font-size: 66px;
    line-height: 1;
    letter-spacing: 5px;
    color: var(--brand-blue);
  }
  .brand-tagline {
    margin-top: 8px;
    font-family: "Andika", sans-serif;
    font-size: 17px;
    letter-spacing: 1.5px;
    color: var(--tagline-orange);
  }
  .contact-band {
    position: absolute;
    left: 0;
    right: 0;
    top: 386px;
    height: 118px;
    background: var(--band-tint);
    border-top: 3px solid var(--rule-blue);
    border-bottom: 3px solid var(--rule-blue);
    text-align: center;
    font-family: "Caprasimo", serif;
    padding-top: 6px;
  }
  .contact-name {
    font-size: 30px;
    line-height: 36px;
    color: var(--name-orange);
  }
  .contact-line {
    font-size: 23px;
    line-height: 33px;
    color: var(--contact-red);
  }
  .business-number {
    position: absolute;
    left: 0;
    right: 0;
    top: 504px;
    height: 40px;
    line-height: 36px;
    text-align: center;
    font-family: "Caprasimo", serif;
    font-size: 17px;
    color: var(--contact-red);
    background: var(--band-tint);
    border-bottom: 3px solid var(--rule-blue);
  }
</style>
</head>
<body>
  <main class="card">
    <div class="card-pattern" role="img" aria-label="Bright party pattern of overlapping teal, pink, yellow, lime and purple rings and dots"></div>
    <div class="party-characters" role="img" aria-label="Illustrated children in costume: a fairy with a wand, a clown doing a handstand and a pirate with a sword"></div>

    <header class="brand">
      <div class="brand-name">Brixtopia</div>
      <div class="brand-tagline">Kids Parties &amp; Events</div>
    </header>

    <section class="contact-band">
      <div class="contact-name">Tilda</div>
      <div class="contact-line">T: 0498 765 210</div>
      <div class="contact-line">E: enquiries@brixtopia.com.au</div>
    </section>

    <footer class="business-number">ABN: 43 527 806 214</footer>
  </main>
</body>
</html>
```